Retail Jewelry Business Card Design Project

We are in need of a new business card design for a retail jewelry store. This store is in the business of fine jewelry including but not specific to bridal jewelry, diamonds, designer jewelry and watches.

This store has been in business for 20 years but continues to strive for a modern professional appeal. The main colors use for this business are a royal blue, white and silver.

Target Market(s)

Target market is ages 18-50

Industry/Entity Type

Jewelry

Requirements
Must have
• Sales Person Name
Sales Person Email Address

Store Address
Store Phone
Website

Standard business card size. No odd shapes or sizes.
Nice to have
• Overall modern feel for card.

We have thought that a design with a nice feature of the logo on the back of the card would be nice but open to ideas.
Should not have
• No specific images of jewelry should be used.

```html
<!DOCTYPE html>
<html lang="en">
<head>
<meta charset="utf-8">
<title>Adrian Marsh Fine Jewelry – Business Card</title>
<link rel="stylesheet" href="https://fonts.googleapis.com/css2?family=Josefin+Sans:wght@400;600&display=swap">
<style>
  :root {
    --royal-navy: #151a47;
    --royal-deep: #0c0f33;
    --card-white: #ffffff;
    --silver: #e9ebf2;
    --silver-soft: rgba(233, 235, 242, 0.22);
    --ink-blue: #24296b;
    --backdrop: #eceef3;
  }
  html, body {
    margin: 0;
    padding: 0;
    overflow: hidden;
  }
  body {
    width: 1200px;
    height: 675px;
    background: var(--backdrop);
    font-family: "Josefin Sans", sans-serif;
    position: relative;
  }
  .card {
    position: absolute;
    top: 75px;
    width: 300px;
    height: 525px;
    box-shadow: 0 6px 18px rgba(20, 24, 60, 0.18);
    overflow: hidden;
  }
  .card--front {
    left: 255px;
    background: linear-gradient(160deg, var(--royal-navy) 0%, var(--royal-deep) 100%);
    color: var(--silver);
  }
  .card--back {
    left: 645px;
    background: var(--card-white);
    color: var(--ink-blue);
  }
  .ornament-area {
    position: absolute;
    left: 50%;
    transform: translateX(-50%);
    width: 210px;
    height: 12px;
    border-radius: 6px;
    background: linear-gradient(90deg, transparent 0%, var(--silver-soft) 50%, transparent 100%);
  }
  .ornament-area--top { top: 46px; }
  .ornament-area--bottom { bottom: 46px; }
  .brand {
    position: absolute;
    left: 0;
    right: 0;
    margin: 0;
    text-align: center;
    font-weight: 400;
    line-height: 1;
  }
  .card--front .brand { top: 218px; color: var(--silver); }
  .card--back .brand { top: 52px; color: var(--ink-blue); }
  .brand__name {
    display: block;
    font-size: 38px;
    letter-spacing: 0.5px;
  }
  .card--back .brand__name { font-size: 30px; }
  .brand__line {
    display: block;
    margin-top: 10px;
    font-size: 15px;
    letter-spacing: 3px;
    text-transform: uppercase;
  }
  .card--back .brand__line { font-size: 12px; margin-top: 8px; }
  .contact {
    position: absolute;
    top: 178px;
    left: 0;
    right: 0;
    text-align: center;
    font-size: 14px;
    line-height: 1.55;
  }
  .contact p { margin: 0; }
  .contact .contact__name {
    font-size: 18px;
    font-weight: 600;
  }
  .contact .contact__title {
    font-size: 13px;
    margin-top: 2px;
  }
  .contact__rule {
    width: 130px;
    height: 1px;
    border: 0;
    background: var(--ink-blue);
    margin: 8px auto 12px;
  }
  .contact .contact__group { margin-top: 14px; }
</style>
</head>
<body>

  <section class="card card--front" aria-label="Card front">
    <div class="ornament-area ornament-area--top" role="img" aria-label="Decorative divider ornament"></div>

    <h1 class="brand">
      <span class="brand__name">Adrian Marsh</span>
      <span class="brand__line">Fine Jewelry</span>
    </h1>

    <div class="ornament-area ornament-area--bottom" role="img" aria-label="Decorative divider ornament"></div>
  </section>

  <section class="card card--back" aria-label="Card back">
    <h2 class="brand">
      <span class="brand__name">Adrian Marsh</span>
      <span class="brand__line">Fine Jewelry</span>
    </h2>

    <div class="contact">
      <p class="contact__name">Adrian Marsh Whitfield</p>
      <p class="contact__title">President</p>
      <hr class="contact__rule">
      <p>2280 Lindell Avenue</p>
      <p>Bayview, FL 32409</p>
      <p class="contact__group">(850) 555-0184</p>
      <p class="contact__group">adrian@adrianmarshjewelry.com</p>
      <p>www.adrianmarshjewelry.com</p>
    </div>
  </section>

</body>
</html>
```